Software company WebSite Design (enterprise level SW, Mobile apps, HW prototypes)

We need design for our new webpages. We got new logo and new business cards and we need webdesign which will be match with those two.
We are dealing with corporate level software development - enterprise level portals, development of optimalization SW, route planning optimalizations. For a few months we are developing mobile applications for companies.
IMPORTANT is to express the cutting edge technological company.

Target Market(s)

IT company customers

Industry/Entity Type

Business

Number of Pages Required

2 page

Requirements
Must have
• Project needs to have landing page and product detail page. Design needs to be created including full font and example images as there would be a real webpage. Design should be clean, modern and expressing hi-tech level of the company.
• Example of well designer web pages - www.quolvent.com, www.brandovi.com - We like the font formatting and font designs (colors, placing, etc - its professional).
• Attached image contains screenshot from old web landing page. It contains basic sections of our business (Simulation Tools, Enterprise Intranet Systems, Hi-tech web presentations, Supporting Enterprise services - Optimalization and logistics monitoring)

```html
<!DOCTYPE html>
<html lang="en">
<head>
<meta charset="utf-8">
<title>KORVA Solutions – Enterprise Software</title>
<link href="https://fonts.googleapis.com/css2?family=Roboto+Slab:wght@300;400;700&family=Roboto:wght@400;500&display=swap" rel="stylesheet">
<style>
:root{
  --navy:#0b3c7d;
  --teal:#33b8c4;
  --cyan:#4fc3e8;
  --yellow:#fbc02d;
  --charcoal:#444648;
  --ink:#1b1b1b;
  --light:#d9f3f7;
  --orange:#f28a1e;
}
*{box-sizing:border-box;margin:0;padding:0}
html,body{width:1200px;height:1200px;overflow:hidden}
body{font-family:"Roboto Slab",serif;color:var(--ink);position:relative;background:var(--light)}
.hero{position:absolute;left:0;top:0;width:1200px;height:602px;
  background:radial-gradient(ellipse at 50% 35%,#d8dde2 0%,#9aa3ab 45%,#3f4650 100%)}
.hero-shade{position:absolute;left:0;top:0;width:1200px;height:602px;
  background:linear-gradient(180deg,rgba(0,0,0,0) 40%,rgba(10,20,35,.55) 100%)}
.site-header{position:absolute;left:230px;top:0;width:741px;height:110px;background:#fff;box-shadow:0 2px 6px rgba(0,0,0,.25)}
.brand{position:absolute;left:0;top:0;width:252px;height:80px;background:var(--charcoal);display:flex;align-items:center;justify-content:center;gap:10px}
.brand-mark{width:22px;height:22px;background:var(--orange)}
.brand-name{color:#fff;font-family:"Roboto",sans-serif;font-weight:500;font-size:30px;letter-spacing:1px}
.callout{position:absolute;left:269px;top:25px;font-size:11px;color:var(--ink)}
.callout .call{color:var(--teal);font-size:10px}
.callout .phone{color:var(--navy);font-size:14px;font-weight:400}
.btn-top{position:absolute;height:28px;background:#e7e7e7;border-top:2px solid #bbb;font-size:9.5px;display:flex;align-items:center;justify-content:center}
.social{position:absolute;left:581px;top:55px;font-size:10px;color:var(--teal);display:flex;align-items:center;gap:6px}
.social i{display:block;width:10px;height:10px;border-radius:50%;background:var(--navy)}
.main-nav{position:absolute;left:0;top:80px;width:741px;height:30px;display:flex;align-items:center;justify-content:center;font-size:10.5px;gap:5px}
.main-nav .sep{color:var(--orange)}
.hero-copy{position:absolute;left:0;top:404px;width:1200px;text-align:center;color:#fff}
.hero-copy h1{font-size:40px;font-weight:700;line-height:44px;letter-spacing:-.5px}
.hero-copy h2{font-size:28px;font-weight:700;line-height:30px}
.hero-copy p{font-size:20px;font-weight:300;color:var(--cyan);margin-top:10px}
.scroll-icon{position:absolute;left:592px;top:523px}
.services{position:absolute;left:239px;top:562px;width:722px;height:305px;display:flex;box-shadow:0 6px 14px rgba(0,0,0,.2)}
.card{width:241px;height:305px;background:var(--navy);color:#fff}
.card.alt{background:var(--teal)}
.card-media{height:152px}
.card h3{font-size:22px;line-height:20px;font-weight:700;margin:14px 0 0 12px}
.card p{font-size:9.5px;line-height:10.5px;margin:12px 10px 0 12px}
.card .cta{display:inline-flex;align-items:center;justify-content:center;width:110px;height:32px;margin:13px 0 0 12px;background:var(--yellow);color:var(--ink);font-size:9.5px}
.tagline{position:absolute;left:238px;top:930px;font-size:45px;font-weight:700;line-height:42.5px;letter-spacing:-1px}
.tagline .t{color:var(--teal)}
.tagline .n{color:var(--navy)}
.welcome{position:absolute;left:598px;top:936px;width:360px}
.welcome h2{font-size:25px;font-weight:300;line-height:30px}
.welcome h2 b{font-weight:700}
.welcome p{font-size:14.6px;line-height:16.6px;font-weight:300;margin-top:4px}
.welcome p b{font-weight:400}
.footer-band{position:absolute;left:0;top:1176px;width:1200px;height:24px;background:var(--teal)}
</style>
</head>
<body>
<div class="hero" role="img" aria-label="Photo of three businessmen discussing work at a desk in a bright office"></div>
<div class="hero-shade"></div>

<header class="site-header">
  <div class="brand"><span class="brand-mark"></span><span class="brand-name">KORVA</span></div>
  <div class="callout">Can't find what you're looking for?<br><span class="call">CALL US</span> <span class="phone">555.214.380</span></div>
  <div class="btn-top" style="left:608px;top:6px;width:62px">REGISTER</div>
  <div class="btn-top" style="left:678px;top:6px;width:50px">SIGN IN</div>
  <div class="btn-top" style="left:441px;top:46px;width:129px">REQUEST SAMPLE PACK</div>
  <div class="social">STAY CONNECTED <i></i><i></i><i></i></div>
  <nav class="main-nav">
    <span>SIMULATION TOOLS</span><span class="sep">/</span>
    <span>ENTERPRISE INTRANET</span><span class="sep">/</span>
    <span>HI-TECH PRESENTATIONS</span><span class="sep">/</span>
    <span>ENTERPRISE</span><span class="sep">/</span>
    <span>OPTIMALIZATION &amp; LOGISTICS</span><span class="sep">/</span>
    <span>CONTACT US</span>
  </nav>
</header>

<section class="hero-copy">
  <h1>LIKE TO ENTERPRISE SERVICES.</h1>
  <h2>HI-TECH WEB PRESENTATIONS</h2>
  <p>EXPLORE BEST SOFTWARE SERVICES PACKAGES</p>
</section>
<svg class="scroll-icon" width="16" height="24" viewBox="0 0 16 24"><rect x="1.5" y="1.5" width="13" height="21" rx="6.5" fill="none" stroke="#f28a1e" stroke-width="2"/><line x1="8" y1="6" x2="8" y2="10" stroke="#f28a1e" stroke-width="2"/></svg>

<section class="services">
  <article class="card">
    <div class="card-media" role="img" aria-label="Hand typing on a keyboard with a glowing world network map" style="background:linear-gradient(135deg,#7fb4e6,#1d4f9a 60%,#0c2450)"></div>
    <h3>SIMULATION<br>TOOLS</h3>
    <p>Lorem ipsum dolor sit amet, consectetur adipisicing elit, sed do eiusmod tempor incididunt ut labore et dolore magna aliqua.</p>
    <span class="cta">START YOUR WORK</span>
  </article>
  <article class="card alt">
    <div class="card-media" role="img" aria-label="Colourful app tiles illustration with a software development banner" style="background:linear-gradient(135deg,#1b8fd0,#2d3e8c 40%,#e0282e 55%,#f7b500 75%,#2aa748)"></div>
    <h3>ENTERPRISE<br>INTRANET SYSTEMS</h3>
    <p>Lorem ipsum dolor sit amet, consectetur adipisicing elit, sed do eiusmod tempor incididunt ut labore et dolore magna aliqua.</p>
    <span class="cta">VIEW ALL PRODUCTS</span>
  </article>
  <article class="card">
    <div class="card-media" role="img" aria-label="Young team working together at computer screens" style="background:linear-gradient(135deg,#e8eef0,#b7c3c7 50%,#d97a8a)"></div>
    <h3>HI-TECH WEB<br>PRESENTATIONS</h3>
    <p>Lorem ipsum dolor sit amet, consectetur adipisicing elit, sed do eiusmod tempor incididunt ut labore et dolore magna aliqua.</p>
    <span class="cta">READ MORE</span>
  </article>
</section>

<h2 class="tagline"><span class="t">SMALL ENOUGH</span><br><span class="n">TO CARE.</span><br><span class="t">BIG ENOUGH</span><br><span class="n">TO COPE.</span></h2>

<section class="welcome">
  <h2>WELCOME TO <b>KORVA.</b></h2>
  <p><b>KORVA Solutions</b> Lorem Ipsum is simply dummy text of the printing and typesetting industry. Lorem Ipsum has been the industry's standard dummy text ever since the 1500s, when an unknown printer took a galley of type and scrambled it to make a type specimen book. It has survived not only five centuries, but also the leap into electronic typesetting, remaining essentially unchanged. It was popularised in the 1960s with the release of Letraset sheets containing Lorem Ipsum.</p>
</section>

<div class="footer-band"></div>
</body>
</html>
```